Flyer-Design für Amerikanische Chiropraktik
Zielgruppe
Praxis für Amerikanische Chiropraktik
Zielgruppe: Gesundheitsbewusste Menschen, gerne gebildet, Affinität zu Sport/Yoga etc.
Flyer soll modern und hochwertig sein (Zielgruppe auch Privatversicherte und Büroleute)
Aufgabenstellung
Bitte keine Schnörkel.
Klare Linien. Straight einfach
Positive Vibes
Website ist nicht final fertig. Das blau/grau und das Grün wird aber aller Voraussicht nach Weiter verwendet. Falls das rot verwendet wird eher nicht so oft bitte.
Sehr gerne für die Überschriften die gleichen Balken unter den Überschriften für den Flyer verwenden.
Flyer bei Nordra Druck ist 99x210 mm (ich denke mit etwas Spiel am Rand für den Druck.) 6 Seiten.
Auf der letzten Seite (sollte die mittlere Rückseite sein) bitte Kontaktdaten und evtl Portraitbild.

```html
<!DOCTYPE html>
<html lang="de">
<head>
<meta charset="utf-8">
<title>Flyer Amerikanische Chiropraktik – Kasimir Holt</title>
<link href="https://fonts.googleapis.com/css2?family=Fira+Sans:ital,wght@0,400;0,600;0,700;1,700&family=Poppins:ital,wght@0,400;0,500;0,600;0,700;1,600;1,700&display=swap" rel="stylesheet">
<style>
:root{
  --dark:#2b2b2d;
  --gold:#b9a57a;
  --gold-text:#b3a06f;
  --white:#ffffff;
  --ink:#222224;
  --bg:#eeeeee;
  --light:#f2f2f2;
}
*{margin:0;padding:0;box-sizing:border-box}
html,body{width:857px;height:1200px;overflow:hidden;background:var(--bg)}
body{position:relative;font-family:"Fira Sans",sans-serif;color:var(--ink)}
.sheet{position:absolute;left:53px;width:751px;height:530px;box-shadow:0 3px 10px rgba(0,0,0,.22);overflow:hidden}
.sheet--outside{top:47px;background:var(--dark)}
.sheet--inside{top:617px;background:var(--white)}
.panel{position:absolute;top:0;width:250.4px;height:100%;overflow:hidden}
.panel--1{left:0}.panel--2{left:250.3px}.panel--3{left:500.6px}
.dark{background:var(--dark);color:var(--white)}
.photo{position:absolute}
.heading{font-family:"Poppins",sans-serif;font-weight:600;font-size:11.6px;line-height:1.2}
.heading .accent{color:var(--gold-text)}
.bar{display:block;width:53px;height:2px;background:var(--gold);margin-top:8px}
.body{font-size:8.4px;line-height:13.4px}
.gold{color:var(--gold-text)}

/* outside / panel 1 */
.treat-photo{left:0;top:0;width:100%;height:170px;background:linear-gradient(160deg,#e8e4df 0%,#bdb6ad 35%,#3a3a3c 60%,#8a6a48 90%);clip-path:polygon(0 0,100% 0,100% 138px,50% 170px,0 148px)}
.treat-edge{position:absolute;left:0;top:0;width:100%;height:176px;background:var(--gold);clip-path:polygon(0 146px,100% 136px,100% 142px,50% 176px,0 154px)}
.reasons{position:absolute;left:16px;top:186px;width:225px}
.reasons .heading{font-size:11.8px}
.symptoms{list-style:none;margin-top:7px}
.symptoms li{font-size:9.2px;line-height:13.4px;padding-left:12px;position:relative}
.symptoms li::before{content:"";position:absolute;left:0;top:4.5px;width:5px;height:5px;border-radius:50%;background:var(--gold)}
.joints{position:absolute;left:0;top:407px;width:100%;height:123px;background:var(--gold);padding:9px 14px 0}
.joints .heading{font-size:11.6px;color:var(--white);font-weight:500}
.joints p{font-size:8.4px;line-height:13.4px;color:var(--white);margin-top:5px}
.joints b{color:var(--dark);font-weight:700}

/* outside / panel 2 */
.promises{position:absolute;left:20px;top:18px;width:220px;list-style:none}
.promises li{position:relative;padding-left:30px;font-size:8.4px;line-height:13.4px;margin-bottom:13.4px}
.promises svg{position:absolute;left:0;top:1px}
.divider{position:absolute;left:20px;top:208px;width:218px;height:2px;background:var(--gold)}
.contact{position:absolute;left:0;top:226px;width:100%;text-align:center;font-size:8.4px;line-height:15.6px}
.contact .name{font-size:10.2px;font-weight:600;color:var(--gold-text);margin-bottom:2px}
.contact .gap{height:7px}
.contact .web{font-weight:600;color:var(--gold-text);margin-top:4px}
.welcome{position:absolute;left:18px;top:432px;width:110px;text-align:center;font-weight:700;font-size:13px;line-height:15px;color:var(--gold);transform:rotate(-7deg)}
.portrait{left:130px;top:362px;width:110px;height:168px;background:radial-gradient(ellipse at 50% 30%,#e9d9c8 0%,#d8d6d3 30%,#f4f4f4 55%,rgba(43,43,45,0) 75%)}

/* outside / panel 3 */
.cover-gold{position:absolute;left:0;top:0;width:100%;height:418px;background:var(--gold);clip-path:polygon(0 0,100% 0,100% 382px,48% 418px,0 391px)}
.brand{position:absolute;left:0;top:60px;width:100%;display:flex;justify-content:center;align-items:center;gap:6px;font-family:"Poppins",sans-serif;font-weight:500;font-size:12px;letter-spacing:.5px;color:var(--dark)}
.brand-dot{width:12px;height:12px;border:1.5px solid var(--dark);border-radius:50%}
.cover-photo{left:20px;top:104px;width:230px;height:290px;background:linear-gradient(180deg,rgba(185,165,122,0) 0%,#e6d3bf 20%,#f6f4f1 55%,#e8cfc6 100%);clip-path:polygon(0 0,100% 0,100% 278px,38% 290px,0 280px)}
.cover-title{position:absolute;left:0;top:430px;width:100%;text-align:center;font-family:"Poppins",sans-serif;color:var(--white)}
.cover-title .line1{font-size:22px;font-weight:400;line-height:26px}
.cover-title .line2{font-size:22px;font-weight:700;line-height:28px}
.tagline{margin-top:8px;font-size:10.8px;font-weight:500;color:var(--gold);letter-spacing:.2px}

/* inside */
.col{position:absolute;left:14px;top:13px;width:225px}
.col .heading{font-size:11.6px}
.col .body{margin-top:9px}
.col .body + .body{margin-top:13.4px}
.col .sub{margin-top:14px}
.adjust-photo{left:0;top:0;width:100%;height:114px;background:linear-gradient(135deg,#d8d2cc 0%,#f2f0ee 40%,#e4d6c8 65%,#cfc9c2 100%)}
.adjust-edge{position:absolute;left:0;top:114px;width:100%;height:4px;background:var(--gold)}
.mid{position:absolute;left:19px;top:137px;width:218px}
.causes{list-style:none;margin-top:18px}
.causes li{position:relative;padding-left:56px;margin-bottom:12px}
.causes svg{position:absolute;left:0;top:4px}
.causes h4{font-weight:600;font-size:10.2px;line-height:13.4px;color:var(--gold-text)}
.causes p{font-size:8.4px;line-height:13.4px}
.uses{list-style:none;margin-top:9px;padding-left:0}
.uses li{position:relative;padding-left:15px;font-size:8.4px;line-height:13.4px;font-weight:600;color:var(--gold-text)}
.uses li::before{content:"";position:absolute;left:1px;top:4px;width:5px;height:5px;border-radius:50%;background:var(--gold)}
.footer-band{position:absolute;left:0;top:497px;width:100%;height:33px;background:var(--gold);display:flex;align-items:center;justify-content:space-between;padding:0 0;font-family:"Poppins",sans-serif;font-style:italic;font-weight:600;font-size:11px;color:var(--white)}
.footer-band .rule{width:55px;height:1.5px;background:var(--white)}
.footer-item{display:flex;align-items:center;gap:7px}
</style>
</head>
<body>

<!-- Außenseite -->
<section class="sheet sheet--outside">
  <div class="panel panel--1 dark">
    <div class="treat-edge"></div>
    <div class="photo treat-photo" role="img" aria-label="Foto: Chiropraktik-Behandlungsliege mit Aktivator-Instrument"></div>
    <div class="reasons">
      <h2 class="heading">Daher besuchen uns Menschen mit:</h2>
      <span class="bar"></span>
      <ul class="symptoms">
        <li>Chronischer Stress</li><li>Schwindel</li><li>Müdigkeit</li><li>Kopfschmerzen</li><li>Migräne</li>
        <li>Schulter- und Armschmerzen</li><li>Impingement-Syndrom</li><li>Karpaltunnelsyndrom</li>
        <li>Beckenschiefstand</li><li>Tinnitus</li><li>Rückenschmerzen</li><li>Bandscheibenvorfall</li>
        <li>Kribbeln und Taubheit in Händen oder Füßen</li>
      </ul>
    </div>
    <div class="joints">
      <h2 class="heading">Chiropraktik und Gelenke</h2>
      <p><b>Beweglicher!</b> Wir erzeugen schelle Dehnungen der Muskulatur direkt am Gelenk und nehmen den Druck. <b>Leichter!</b> Dabei lösen wir Reflexe aus, die im Gehirn die Funktion zurückbringen. <b>Besser!</b> Unterstützt die Heilung deiner Gelenke und Nervensystem</p>
    </div>
  </div>

  <div class="panel panel--2 dark">
    <ul class="promises">
      <li><svg width="20" height="20" viewBox="0 0 20 20"><circle cx="9" cy="11" r="7.5" fill="none" stroke="#b9a57a" stroke-width="1.8"/><path d="M5 10.5l3.5 3.5L18 3" fill="none" stroke="#b9a57a" stroke-width="2"/></svg>Wir sind Experten auf unserem Gebiet.</li>
      <li><svg width="20" height="20" viewBox="0 0 20 20"><circle cx="9" cy="11" r="7.5" fill="none" stroke="#b9a57a" stroke-width="1.8"/><path d="M5 10.5l3.5 3.5L18 3" fill="none" stroke="#b9a57a" stroke-width="2"/></svg>Arbeiten nach neuesten Wissenschaftlichen Kenntnissen.<br>Sanfte und zielgerichtete Behandlung.</li>
      <li><svg width="20" height="20" viewBox="0 0 20 20"><circle cx="9" cy="11" r="7.5" fill="none" stroke="#b9a57a" stroke-width="1.8"/><path d="M5 10.5l3.5 3.5L18 3" fill="none" stroke="#b9a57a" stroke-width="2"/></svg>Profitieren Sie von langjährige praktische Erfahrung und modernen neurowissenschaftliche Aspekten in der chiropraktischen Behandlung.</li>
      <li><svg width="20" height="20" viewBox="0 0 20 20"><circle cx="9" cy="11" r="7.5" fill="none" stroke="#b9a57a" stroke-width="1.8"/><path d="M5 10.5l3.5 3.5L18 3" fill="none" stroke="#b9a57a" stroke-width="2"/></svg>Wir sind mit Freude und Engagement für Dich und Deine Gesundheit da.</li>
    </ul>
    <div class="divider"></div>
    <address class="contact" style="font-style:normal">
      <div class="name">Kasimir Holt</div>
      <div>Heil- und Chiropraktiker,</div>
      <div>B.Sc. Physiotherapie</div>
      <div class="gap"></div>
      <div>Lindenweg 12 | 83714 Talheim</div>
      <div>Tel: 0151/48209317</div>
      <div>praxis@chiropraktik-holt.de</div>
      <div class="web">www.chiropraktik-holt.de</div>
    </address>
    <p class="welcome">Wir freuen uns auf Dich!</p>
    <div class="photo portrait" role="img" aria-label="Porträtfoto des Chiropraktikers im weißen T-Shirt, sitzend"></div>
  </div>

  <div class="panel panel--3 dark">
    <div class="cover-gold"></div>
    <div class="brand"><span class="brand-dot"></span>Kasimir Holt</div>
    <div class="photo cover-photo" role="img" aria-label="Foto: Chiropraktiker umarmt eine Patientin von vorne"></div>
    <h1 class="cover-title">
      <div class="line1">Dein Weg zu mehr</div>
      <div class="line2">Wohlbefinden</div>
      <div class="tagline">MODERN. URSÄCHLICH. ANDERS</div>
    </h1>
  </div>
</section>

<!-- Innenseite -->
<section class="sheet sheet--inside">
  <div class="panel panel--1">
    <div class="col">
      <h2 class="heading">Was ist <span class="accent">Amerikanische Chiropraktik?</span></h2>
      <span class="bar"></span>
      <p class="body">Amerikanische Chiropraktik ist eine eigenständige, ganzheitliche und vitalistische Form der Gesundheitspflege, die darauf ausgerichtet ist, Gesundheit und Funktion des menschlichen Körpers wiederherzustellen und zu erhalten.</p>
      <p class="body">Sie ist sowohl eine evidenzbasierte Wissenschaft als auch eine Heilkunst und eine Philosophie, die nach der optimalen Funktion des Nervensystems strebt.</p>
      <h2 class="heading sub">Wie funktioniert <span class="accent">Chiropraktik?</span></h2>
      <span class="bar"></span>
      <p class="body">Der Körper wird von seinem Nervensystem gesteuert. Es ist dafür verantwortlich, wie ein Mensch seine Umwelt wahrnimmt und durch das Leben geht. Über das Nervensystem empfängt und sendet das Gehirn fortwährend Informationen an Organe, Muskeln und alle anderen Strukturen. Seine optimale Funktion ist demnach von größter Bedeutung.</p>
      <p class="body">Im besten Fall werden Körper und Psyche über das Nervensystem in Balance gehalten. Dazu muss alles störungsfrei miteinander vernetzt sein. Fehlstellungen und Blockaden können die Vernetzung stören: Es kommt zu sogenannten Subluxationen. Das physische und psychische Gleichgewicht gerät ins Wanken. Die Folgen können sehr vielfältig sein. Muskelverspannungen, Nackenschmerzen, Kopfschmerzen oder Rückenschmerzen können die Folge sein. Oft bleiben solche <span class="gold">Subluxationen</span> über Jahre unbemerkt, bevor sie Schmerzen und/oder psycho-emotionale Symptome verursachen.</p>
    </div>
  </div>

  <div class="panel panel--2 dark">
    <div class="photo adjust-photo" role="img" aria-label="Foto: Hände des Chiropraktikers bei der Justierung am Rücken einer Patientin"></div>
    <div class="adjust-edge"></div>
    <div class="mid">
      <h2 class="heading">Was ist eigentlich eine <span class="accent">Subluxation?</span></h2>
      <span class="bar"></span>
      <p class="body" style="margin-top:9px">Wir definieren eine vertebrale Subluxation als ein dysfunktionales Gebiet in der Wirbelsäule, dass sich aufgrund seines Einflusses auf das Nervensystem negativ auf die Gesundheit und das Wohlbefinden auswirkt. Die Funktion der Wirbelsäule als wichtiger Informationsgeber für das Gehirn ist gestört.</p>
      <h2 class="heading" style="margin-top:16px">Ursachen für eine <span class="accent">Subluxation</span></h2>
      <ul class="causes">
        <li><svg width="40" height="40" viewBox="0 0 40 40" fill="none" stroke="#fff" stroke-width="1.4"><circle cx="20" cy="15" r="8"/><path d="M7 38c0-8 6-13 13-13s13 5 13 13z"/><path d="M4 6l4 3M36 6l-4 3M3 16h4M37 16h-4"/></svg><h4>Physischer Stress</h4><p>wie z.B. Trauma (Brüche etc.) Unfälle, langes Sitzen, Bewegungsmangel</p></li>
        <li><svg width="40" height="40" viewBox="0 0 40 40" fill="none" stroke="#fff" stroke-width="1.4"><circle cx="11" cy="22" r="7"/><circle cx="28" cy="11" r="7"/><circle cx="28" cy="30" r="6"/><circle cx="10" cy="21" r="1.2"/><circle cx="28" cy="11" r="1.2"/><circle cx="28" cy="30" r="1.2"/></svg><h4>Toxischer Stress</h4><p>wie z.B. Zigaretten, Alkohol, Drogen, Abgase, Medikamente, Übersäuerung</p></li>
        <li><svg width="40" height="40" viewBox="0 0 40 40" fill="none" stroke="#fff" stroke-width="1.4"><path d="M14 4h12v6c6 2 10 6 10 12v16H4V22c0-6 4-10 10-12z"/><circle cx="9" cy="12" r="3.5"/><path d="M20 14v24M12 24v14M28 24v14"/></svg><h4>Psychischer Stress</h4><p>Macht einen großen Anteil aus. Druck und hohe Anforderungen im Beruf, Alltagsstress, Schlafmangel, Sorgen, Überforderung.</p></li>
      </ul>
    </div>
  </div>

  <div class="panel panel--3">
    <div class="col">
      <h2 class="heading">Wie helfen wir? <span class="accent">Die Justierung</span></h2>
      <span class="bar"></span>
      <p class="body">Die chiropraktische Justierung korrigiert eine <b class="gold">Subluxation</b>, indem sie das schadhafte neurologische Muster durchbricht. Durch einen sanften und gezielten Impuls wird die physiologische Beweglichkeit und Position eines Gelenkes wieder hergestellt und faszialer Adhäsionen gelöst. Die Impulse führen zu einer messbaren Verbesserung in der Funktion hinsichtlich der Beziehung zwischen Nervensystem und Bewegungsapparat (Lindqvist et al., 2021). Der chiropraktische Impuls wirkt auf struktureller Ebene (am Gelenk) und im Nervensystem. Der Informationsfluss zwischen Körper und Nervensystem wird harmonisiert und Selbstheilungskräfte aktiviert, um dir eine volle Funktionalität und mehr Lebensqualität zu ermöglichen.</p>
      <h2 class="heading" style="margin-top:26px">Für wen?</h2>
      <span class="bar"></span>
      <p class="body">Die Amerikanische Chiropraktik verfolgt einen ganzheitlichen und ursachenbezogenen Ansatz, wodurch sich vielseitige Anwendungsbereiche ergeben. Unser Angebot reicht von Gesundheitsvorsorge bis hin zur Behandlung von bereits existierenden Störungen und Symptomen.Anwendungsgebiete</p>
      <ul class="uses">
        <li>Chiropraktik zur Leistungssteigerung im Sport</li>
        <li>Chiropraktik als konstante Begleitung für mehr Balance und Wohlbefinden im Alltag</li>
        <li>Chiropraktik in der Schwangerschaft</li>
        <li>Chiropraktik als effektive Methode für die Behandlung von Schmerzen und Einschränkungen des Bewegungsapparats und des Nervensystems</li>
      </ul>
    </div>
  </div>

  <footer class="footer-band">
    <div class="footer-item"><span class="rule"></span><span style="margin-left:5px">"Time to Connect Your Brain."</span></div>
    <div class="footer-item">www.chiropraktik-holt.de</div>
    <div class="footer-item"><span style="margin-right:5px">"Time to Connect Your Brain."</span><span class="rule"></span></div>
  </footer>
</section>

</body>
</html>
```